Heritage Depot Business Cards

Require a business card design. <br/><br/>Needs to include logo (either round or long version) plus these details:<br/>Maya Corvell<br/>Heritage Depot<br/>maya@brightmarttrade.com.au<br/>02 6418 7395<br/>PO Box Glenfarrow NSW 2791<br/>www.heritagedepot.com.au<br/><br/>I need in an editable format so that I can create for multiple staff members. <br/><br/>

Target Market(s)

We are an online store selling renovation products to home owners are builders. Looking for a classic classy design.

Industry/Entity Type

Home And Garden

Contact Information for Business Card

Maya Corvell
Heritage Depot
maya@brightmarttrade.com.au
02 6418 7395
PO Box Glenfarrow NSW 2791
www.heritagedepot.com.au

Colors

Designer to choose colors to be used in the design.

Requirements
Must have
• Must include Logo.

```html
<!DOCTYPE html>
<html lang="en">
<head>
<meta charset="utf-8">
<title>Heritage Depot Business Cards</title>
<link href="https://fonts.googleapis.com/css2?family=Roboto:wght@300;400;700&display=swap" rel="stylesheet">
<style>
  :root {
    --stage: #2b2b2b;
    --card: #1d1d1d;
    --silver: #d8d8d8;
    --silver-dim: #9a9a9a;
    --rule: #6a6a6a;
  }
  * { margin: 0; padding: 0; box-sizing: border-box; }
  html, body { width: 1200px; height: 895px; overflow: hidden; background: var(--stage); }
  body { font-family: "Roboto", sans-serif; color: var(--silver); position: relative; }

  .card {
    position: absolute; left: 270px; width: 660px; height: 377px;
    background: var(--card);
    box-shadow: 0 10px 24px rgba(0,0,0,0.55);
    overflow: hidden;
  }
  .card--front { top: 38px; }
  .card--back { top: 470px; }

  .brand { display: flex; align-items: center; gap: 18px; }
  .brand__circle {
    width: 86px; height: 86px; border-radius: 50%;
    border: 2px solid var(--silver); flex-shrink: 0;
  }
  .brand__name { font-weight: 400; color: var(--silver); white-space: nowrap; }

  .card--front .brand {
    position: absolute; left: 50%; top: 50%; transform: translate(-50%, -50%);
  }
  .card--front .brand__circle { width: 120px; height: 120px; }
  .card--front .brand__name { font-size: 44px; }

  .card--back .brand { position: absolute; left: 48px; top: 78px; }
  .card--back .brand__name { font-size: 38px; }

  .holder {
    position: absolute; right: 40px; top: 40px; text-align: right;
    font-weight: 300; font-size: 16px; line-height: 1.3;
  }
  .holder__name { font-weight: 700; font-size: 26px; letter-spacing: 0.5px; margin-bottom: 6px; color: #fff; }

  .divider { position: absolute; left: 48px; right: 40px; top: 218px; height: 1px; background: var(--rule); }

  .contacts {
    position: absolute; left: 48px; bottom: 36px;
    list-style: none; font-weight: 300; font-size: 17px; line-height: 1.55;
  }
  .contacts li { display: flex; align-items: center; gap: 14px; }
  .contacts svg { width: 16px; height: 16px; fill: none; stroke: var(--silver); stroke-width: 1.6; }
</style>
</head>
<body>
  <section class="card card--front">
    <div class="brand">
      <span class="brand__circle"></span>
      <span class="brand__name">Heritage Depot</span>
    </div>
  </section>

  <section class="card card--back">
    <div class="brand">
      <span class="brand__circle"></span>
      <span class="brand__name">Heritage Depot</span>
    </div>

    <div class="holder">
      <p class="holder__name">MAYA CORVELL</p>
      <p>Heritage Depot</p>
      <p>PO Box Glenfarrow</p>
      <p>NSW 2791</p>
    </div>

    <div class="divider"></div>

    <ul class="contacts">
      <li>
        <svg viewBox="0 0 16 16"><path d="M3 2h3l1.5 3.5-2 1.2a8 8 0 0 0 3.8 3.8l1.2-2L14 10v3a1 1 0 0 1-1 1A11 11 0 0 1 2 3a1 1 0 0 1 1-1z"/></svg>
        02 6418 7395
      </li>
      <li>
        <svg viewBox="0 0 16 16"><rect x="1.5" y="3.5" width="13" height="9"/><path d="M1.5 3.5 8 9l6.5-5.5"/></svg>
        maya@brightmarttrade.com.au
      </li>
      <li>
        <svg viewBox="0 0 16 16"><circle cx="8" cy="8" r="6.5"/><ellipse cx="8" cy="8" rx="3" ry="6.5"/><path d="M1.5 8h13"/></svg>
        www.heritagedepot.com.au
      </li>
    </ul>
  </section>
</body>
</html>
```